Business Card Design Project

I need a business card design for our new logo, please check the logo at the following link:
https://www.filecrate.net/s/q7rtx2pw9kd41m/FernLoop.png
The address on the business card:
Av. Gervásio Tavares 418 sala 207
Barra da Tijuca, Rio de Janeiro, RJ
CEP: 22714-380
Brasil
Phone: +55 21 86347215
e-mail: osvaldo@fernloop.com.br
Updates
Thank you all for sending your designs, we will not provide feedback because there are too many designs, on December 3 we will pick the best design according to our point of view. Please keep posting.
Osvaldo
Industry/Entity Type
Business
Look and feel
Each slider illustrates characteristics of the customer's brand and the style your logo design should communicate.

```html
<!DOCTYPE html>
<html lang="pt-BR">
<head>
<meta charset="utf-8">
<title>FernLoop – Cartão de visita</title>
<link rel="stylesheet" href="https://fonts.googleapis.com/css2?family=PT+Sans:ital,wght@0,400;0,700;1,700&display=swap">
<style>
  :root {
    --backdrop: #e8e5e0;
    --card: #ffffff;
    --ink: #231f20;
    --text: #3a3a3a;
    --accent: #f7c81e;
    --band-text: #ffffff;
  }
  * { margin: 0; padding: 0; box-sizing: border-box; }
  html, body {
    width: 960px; height: 1200px; overflow: hidden;
    background: var(--backdrop);
    font-family: "PT Sans", Arial, sans-serif;
  }
  .canvas { position: relative; width: 960px; height: 1200px; }
  .card {
    position: absolute;
    width: 840px; height: 480px;
    background: var(--card);
    border-radius: 32px;
    overflow: hidden;
  }
  .card--front { left: 53px; top: 75px; }
  .card--back { left: 55px; top: 638px; }

  .brand {
    position: absolute; left: 0; right: 0;
    display: flex; align-items: center; justify-content: center; gap: 18px;
    font-weight: 700; color: var(--ink); letter-spacing: 1px;
  }
  .brand__dot { border-radius: 50%; background: var(--accent); flex: none; }
  .card--front .brand { top: 145px; font-size: 74px; line-height: 1; }
  .card--front .brand__dot { width: 40px; height: 40px; }
  .card--back .brand { top: 175px; font-size: 120px; line-height: 1; }
  .card--back .brand__dot { width: 64px; height: 64px; }

  .contact {
    position: absolute; left: 0; right: 0; top: 264px;
    text-align: center; color: var(--text); font-size: 22px; line-height: 39px;
  }
  .contact__name { font-size: 25px; font-weight: 700; }
  .contact__role { font-size: 21px; }
  .contact__label { font-weight: 700; font-style: italic; }

  .swoosh { position: absolute; left: 0; top: 0; width: 840px; height: 480px; }
  .address {
    position: absolute; left: 0; right: 0; top: 436px;
    text-align: center; color: var(--band-text); font-size: 20px; line-height: 22px;
  }
</style>
</head>
<body>
<main class="canvas">
  <section class="card card--front">
    <svg class="swoosh" viewBox="0 0 840 480" aria-hidden="true">
      <path d="M0,414 Q420,359 840,421 L840,480 L0,480 Z" fill="var(--accent)"/>
      <path d="M0,422 Q420,368 840,429 L840,480 L0,480 Z" fill="var(--card)"/>
      <path d="M0,430 Q420,376 840,436 L840,480 L0,480 Z" fill="var(--ink)"/>
    </svg>
    <div class="brand"><span class="brand__dot"></span><span class="brand__name">FernLoop</span></div>
    <div class="contact">
      <p><span class="contact__name">Your Name -</span> <span class="contact__role">Designation</span></p>
      <p><span class="contact__label">t</span> : +55 21 86347215</p>
      <p><span class="contact__label">e</span> : osvaldo@fernloop.com.br &nbsp;|&nbsp; <span class="contact__label">w</span> : www.fernloop.com.br</p>
    </div>
    <address class="address" style="font-style:normal">
      Av. Gervásio Tavares 418 sala 207,<br>
      Barra da Tijuca, Rio de Janeiro, RJ, CEP: 22714-380, Brasil
    </address>
  </section>

  <section class="card card--back">
    <div class="brand"><span class="brand__dot"></span><span class="brand__name">FernLoop</span></div>
  </section>
</main>
</body>
</html>
```